Company or website name
- www.tapwellHOMEfind.com
- Links to the website
- tapwellhomefind.com
- Describe your company and organization and target audience
- My name is calvin brisk from houston texas. I am a realtor. I have been trying very hard to develop a site that not only reflects me but can generate some business. I have a site with an idx search but it is too expensive and I really dont think IDX is the way to go. I just want a site that is neat and holds people interest. For this contest, I pretty much did all the work. I need your creativity. I have a drop box link that has everything in it. Each section is marked. I have about me, about what I do, How i am different, Neighborhoods i specialize in etc.
- The design should have the following
- I want in my site the following: I would Live Feed of my Snapvane and Friendloop page on the first main page I want my video playing as the main shot. I have 2 give a ways (something of value), buyers handbook and sellers handbook I do a monthly newsletter i would also like to give some attention to. I want a chat box that is either a bot or goes into text message to me www.tapwellHOMEfind.com is the website url dropbox link: https://www.boxlockerhub.com/sh/7kqp2n48vtzz15r/BBLmr_3pH27hkwQTqN9dYfLtB?dl=0 If you can use the idx's that my assocation provides that would be great. I have been told they are frames, it is ok if you dont but if you can they do have some great info.

```html
<!DOCTYPE html>
<html lang="en">
<head>
<meta charset="utf-8">
<title>tapwellhomefind.com — Calvin Brisk, Houston Realtor</title>
<link href="https://fonts.googleapis.com/css2?family=Roboto+Slab:wght@400;700&family=Open+Sans:wght@400;600;700&display=swap" rel="stylesheet">
<style>
:root{
  --red:#c8202f;
  --red-dark:#a91824;
  --ink:#2b2b2b;
  --muted:#6b6b6b;
  --topbar:#1e1e1e;
  --footer:#2f2f2f;
  --panel:#ebebeb;
  --line:#d6d6d6;
  --white:#ffffff;
}
*{box-sizing:border-box;margin:0;padding:0}
html,body{width:1200px;height:3569px;overflow:hidden}
body{position:relative;font-family:"Open Sans",Arial,sans-serif;color:var(--ink);background:var(--white)}
section,header,footer{position:absolute;left:0;width:1200px}

/* top bar */
.topbar{top:0;height:36px;background:var(--topbar);color:#cfcfcf;font-size:11px}
.topbar .help{position:absolute;left:24px;top:11px}
.topbar nav{position:absolute;left:330px;top:0;display:flex;height:36px}
.topbar nav a{color:#fff;text-decoration:none;padding:0 16px;line-height:36px;font-size:13px;font-weight:600}
.topbar nav a.active{background:var(--red)}
.topbar .account{position:absolute;right:24px;top:11px}

/* brand header */
.brand{top:36px;height:99px;background:var(--white);text-align:center}
.brand .name{display:inline-flex;align-items:center;gap:10px;margin-top:24px;font-family:"Roboto Slab",Georgia,serif;font-weight:700;font-size:32px;color:var(--ink)}
.brand .name i{display:inline-block;width:18px;height:18px;background:var(--red)}
.brand .tagline{font-size:13px;color:var(--muted);margin-top:4px}

/* hero */
.hero{top:135px;height:555px;background:linear-gradient(180deg,#4a5566 0%,#6c7280 45%,#3d3a36 100%)}
.hero .play{position:absolute;left:566px;top:256px}
.hero .agent{position:absolute;width:100%;top:420px;text-align:center;color:#fff;font-size:22px;font-family:"Roboto Slab",Georgia,serif}
.hero h1{position:absolute;width:100%;top:455px;text-align:center;color:#fff;font-family:"Roboto Slab",Georgia,serif;font-weight:700;font-size:58px;letter-spacing:1px;white-space:nowrap}
.searchband{top:690px;height:115px;background:var(--red)}
.searchband .field{position:absolute;left:390px;top:36px;width:420px;height:42px;background:#fff;border-radius:3px;font-size:13px;color:#8a8a8a;padding:12px 16px}
.searchband .field svg{position:absolute;right:14px;top:12px}

/* agent intro */
.intro{top:805px;height:535px}
.intro .photo{position:absolute;left:180px;top:25px;width:245px;height:300px;background:linear-gradient(180deg,#b9bcc2,#5e636c)}
.intro .phone{position:absolute;left:180px;top:325px;width:245px;height:36px;background:var(--red);color:#fff;font-weight:700;font-size:15px;display:flex;align-items:center;justify-content:center;gap:8px}
.intro .agent-name{position:absolute;left:180px;width:245px;top:378px;text-align:center;font-weight:700;font-size:16px;letter-spacing:1px}
.intro .agent-title{position:absolute;left:160px;width:285px;top:402px;text-align:center;font-size:10px;color:var(--muted);white-space:nowrap}
.intro .social{position:absolute;left:180px;width:245px;top:424px;display:flex;justify-content:center;gap:8px}
.intro .social span{width:22px;height:22px;border-radius:50%;background:var(--ink)}
.intro h2{position:absolute;left:470px;top:55px;font-family:"Roboto Slab",Georgia,serif;font-size:36px;font-weight:700;white-space:nowrap}
.intro .lead{position:absolute;left:470px;top:108px;font-size:16px;color:var(--ink)}
.intro ul{position:absolute;left:470px;top:150px;list-style:none}
.intro li{display:flex;align-items:center;gap:12px;font-size:14px;color:#444;height:30px}

/* shared headings */
.section-title{position:absolute;width:100%;text-align:center;font-family:"Roboto Slab",Georgia,serif;font-weight:700;font-size:36px}

/* featured listings */
.listings{top:1340px;height:450px;background:var(--panel)}
.listings .section-title{top:38px}
.card{position:absolute;top:95px;width:290px;height:325px;background:#fff;box-shadow:0 1px 3px rgba(0,0,0,.15)}
.card .head{height:30px;padding:0 10px;display:flex;align-items:center;gap:8px;font-size:13px;font-weight:700;color:var(--red);border-top:3px solid var(--red);white-space:nowrap}
.card .head b{background:var(--red);color:#fff;font-size:10px;padding:2px 6px}
.card .city{font-size:11px;color:var(--muted);padding:0 10px;height:16px}
.card .img{height:160px;background:linear-gradient(180deg,#9cb6cf,#6f8a5a)}
.card .avatar{position:absolute;left:12px;top:180px;width:48px;height:48px;border-radius:50%;background:#9a8f86;border:3px solid #fff}
.card .stats{position:absolute;top:236px;left:0;width:100%;display:flex;justify-content:space-around;font-size:11px;color:var(--muted);border-top:1px solid var(--line);border-bottom:1px solid var(--line);padding:8px 0}
.card .price{position:absolute;top:284px;left:12px;font-size:22px;font-weight:700}
.listings .pager{position:absolute;left:1030px;top:428px;display:flex;gap:5px}
.listings .pager span{width:10px;height:10px;border:1px solid #999;background:#fff}

/* recent posts */
.posts{top:1790px;height:400px}
.posts .section-title{top:38px}
.post{position:absolute;top:95px;width:270px;text-align:center}
.post .img{height:160px}
.post h3{font-family:"Roboto Slab",Georgia,serif;font-size:20px;color:var(--red);margin-top:14px}
.post p{font-size:14px;color:var(--ink);margin-top:2px}

/* communities */
.communities{top:2190px;height:510px;background:var(--panel)}
.communities .figure{position:absolute;left:70px;top:120px;width:360px;height:390px;background:linear-gradient(180deg,#d9c7b8,#8a5a4a)}
.communities h2{position:absolute;left:540px;top:45px;width:460px;text-align:center;font-family:"Roboto Slab",Georgia,serif;font-weight:700;font-size:36px;white-space:nowrap}
.communities .sub{position:absolute;left:540px;top:98px;width:460px;text-align:center;font-size:14px;color:var(--muted)}
.area{position:absolute;width:150px;text-align:center;font-size:14px}
.area .img{width:104px;height:104px;border-radius:50%;margin:0 auto 10px;border:4px solid #fff;background:linear-gradient(180deg,#a9bfd0,#6f7f63)}

/* social feeds */
.feeds{top:2700px;height:510px;border-top:6px solid var(--red)}
.snap{position:absolute;left:290px;top:55px;width:490px;height:400px;border:1px solid var(--line);background:#fff}
.snap .mark{position:absolute;left:-22px;top:-22px;width:62px;height:62px;background:var(--red);border-radius:12px}
.snap .handle{position:absolute;left:60px;top:18px;font-weight:700;font-size:15px}
.snap .follow{position:absolute;left:300px;top:16px;border:1px solid var(--line);font-size:11px;padding:3px 12px;border-radius:3px}
.snap .stats{position:absolute;left:60px;top:44px;font-size:11px;color:var(--muted)}
.snap .bio{position:absolute;left:60px;top:62px;width:380px;font-size:11px;color:#3a6fa0;line-height:15px}
.snap .grid{position:absolute;left:60px;top:110px;display:grid;grid-template-columns:repeat(3,110px);gap:8px}
.snap .grid div{height:84px}
.friend{position:absolute;left:800px;top:55px;width:160px;height:395px;border:1px solid var(--line);background:#fff}
.friend .cover{height:70px;background:linear-gradient(180deg,#8ea6bf,#5a6e52)}
.friend .name{font-size:11px;font-weight:700;padding:8px;color:#3b5998;white-space:nowrap}
.friend .line{height:7px;background:#e2e2e2;margin:7px 8px}
.friend .pic{height:100px;margin:8px;background:linear-gradient(180deg,#b7c4cf,#7a8a6c)}

/* footer */
.footer{top:3210px;height:359px;background:var(--footer);color:#cfcfcf;text-align:center;font-size:12px;line-height:22px}
.footer .info{padding-top:70px}
.footer .rule{width:700px;height:1px;background:#555;margin:28px auto 18px}
</style>
</head>
<body>

<header class="topbar">
  <div class="help">Questions? We're here to help. Call: 713-555-0148</div>
  <nav>
    <a class="active">Home</a><a>Search</a><a>Sell</a><a>Communities</a><a>Market Insider</a><a>Resources</a><a>About</a>
  </nav>
  <div class="account">Contact · Login · Sign In</div>
</header>

<header class="brand">
  <div class="name"><i></i>www.tapwellHOMEfind.com</div>
  <div class="tagline">Calvin, Your Favorite Realtor</div>
</header>

<section class="hero" role="img" aria-label="Video still of a two-storey family home at dusk with lit windows">
  <svg class="play" width="68" height="68" viewBox="0 0 68 68" aria-hidden="true">
    <circle cx="34" cy="34" r="31" fill="rgba(0,0,0,.25)" stroke="#fff" stroke-width="3"/>
    <path d="M27 21 L49 34 L27 47 Z" fill="#fff"/>
  </svg>
  <div class="agent">Calvin Brisk</div>
  <h1>DISCOVER YOUR DREAM HOME</h1>
</section>

<section class="searchband">
  <div class="field">Search for your dream home
    <svg width="16" height="16" viewBox="0 0 16 16" aria-hidden="true"><circle cx="6.5" cy="6.5" r="5" fill="none" stroke="#888" stroke-width="2"/><path d="M10.5 10.5 L15 15" stroke="#888" stroke-width="2"/></svg>
  </div>
</section>

<section class="intro">
  <div class="photo" role="img" aria-label="Portrait photo of agent Calvin Brisk"></div>
  <div class="phone">
    <svg width="14" height="14" viewBox="0 0 24 24" aria-hidden="true"><path fill="#fff" d="M6.6 10.8a15.1 15.1 0 0 0 6.6 6.6l2.2-2.2a1 1 0 0 1 1-.25 11.4 11.4 0 0 0 3.6.57 1 1 0 0 1 1 1V20a1 1 0 0 1-1 1A17 17 0 0 1 3 4a1 1 0 0 1 1-1h3.5a1 1 0 0 1 1 1c0 1.25.2 2.45.57 3.6a1 1 0 0 1-.25 1z"/></svg>
    713-555-0148
  </div>
  <div class="agent-name">CALVIN BRISK</div>
  <div class="agent-title">CRS, Luxury, CPRES | Brightpath Realty Memorial</div>
  <div class="social"><span></span><span></span><span></span></div>

  <h2>Your Local Real Estate Connection</h2>
  <p class="lead">Get a positive, helpful partner for buying or selling a home.</p>
  <ul>
    <li><svg width="14" height="14" viewBox="0 0 14 14" aria-hidden="true"><path d="M2 7l3 3 7-7" fill="none" stroke="#c8202f" stroke-width="2"/></svg>Trusted resource for answers about the process</li>
    <li><svg width="14" height="14" viewBox="0 0 14 14" aria-hidden="true"><path d="M2 7l3 3 7-7" fill="none" stroke="#c8202f" stroke-width="2"/></svg>Innovative marketing strategies</li>
    <li><svg width="14" height="14" viewBox="0 0 14 14" aria-hidden="true"><path d="M2 7l3 3 7-7" fill="none" stroke="#c8202f" stroke-width="2"/></svg>Expertise about neighborhood features</li>
    <li><svg width="14" height="14" viewBox="0 0 14 14" aria-hidden="true"><path d="M2 7l3 3 7-7" fill="none" stroke="#c8202f" stroke-width="2"/></svg>Skilled at budget home searches</li>
    <li><svg width="14" height="14" viewBox="0 0 14 14" aria-hidden="true"><path d="M2 7l3 3 7-7" fill="none" stroke="#c8202f" stroke-width="2"/></svg>Strong negotiation skills</li>
    <li><svg width="14" height="14" viewBox="0 0 14 14" aria-hidden="true"><path d="M2 7l3 3 7-7" fill="none" stroke="#c8202f" stroke-width="2"/></svg>Support through the closing and beyond</li>
  </ul>
</section>

<section class="listings">
  <h2 class="section-title">Featured Listings</h2>
  <article class="card" style="left:155px">
    <div class="head"><b>FEATURED</b>2721 Larkmoor Drive</div>
    <div class="city">Houston, TX 77099</div>
    <div class="img" role="img" aria-label="Listing photo of a brick home"></div>
    <div class="avatar" role="img" aria-label="Listing agent photo"></div>
    <div class="stats"><span>4 Beds</span><span>3 Baths</span><span>2,740 sq ft</span></div>
    <div class="price">$399,000</div>
  </article>
  <article class="card" style="left:470px">
    <div class="head"><b>FEATURED</b>3605 Fernhollow Drive</div>
    <div class="city">Houston, TX 77099</div>
    <div class="img" role="img" aria-label="Listing photo of a two-storey home"></div>
    <div class="avatar" role="img" aria-label="Listing agent photo"></div>
    <div class="stats"><span>4 Beds</span><span>3 Baths</span><span>2,910 sq ft</span></div>
    <div class="price">$295,000</div>
  </article>
  <article class="card" style="left:785px">
    <div class="head"><b>FEATURED</b>2721 Larkmoor Drive</div>
    <div class="city">Houston, TX 77099</div>
    <div class="img" role="img" aria-label="Listing photo of a home with a front lawn"></div>
    <div class="avatar" role="img" aria-label="Listing agent photo"></div>
    <div class="stats"><span>4 Beds</span><span>3 Baths</span><span>2,740 sq ft</span></div>
    <div class="price">$399,000</div>
  </article>
  <div class="pager"><span></span><span></span></div>
</section>

<section class="posts">
  <h2 class="section-title">Recent Posts</h2>
  <article class="post" style="left:155px">
    <div class="img" role="img" aria-label="Photo of a bright living room" style="background:linear-gradient(180deg,#d8cbb8,#8c7560)"></div>
    <h3>5 DIY Improvements</h3><p>To Make Your Home Cleaner</p>
  </article>
  <article class="post" style="left:465px">
    <div class="img" role="img" aria-label="Photo of a house with a porch" style="background:linear-gradient(180deg,#a9c0d4,#6e7c5e)"></div>
    <h3>Choosing</h3><p>the Right Home</p>
  </article>
  <article class="post" style="left:775px">
    <div class="img" role="img" aria-label="Photo of a modern kitchen" style="background:linear-gradient(180deg,#c9c6c0,#5d5a55)"></div>
    <h3>When to Get Excited</h3><p>About the Housing Market</p>
  </article>
</section>

<section class="communities">
  <div class="figure" role="img" aria-label="Photo of a smiling woman pointing toward the community list"></div>
  <h2>Communities We Served</h2>
  <p class="sub">Proudly serving the following communities:</p>
  <div class="area" style="left:590px;top:150px"><div class="img" role="img" aria-label="Bellaire area homes"></div>Bellaire Area</div>
  <div class="area" style="left:830px;top:150px"><div class="img" role="img" aria-label="Meyerland area homes"></div>Meyerland Area</div>
  <div class="area" style="left:590px;top:310px"><div class="img" role="img" aria-label="Museum District buildings"></div>Museum District</div>
  <div class="area" style="left:830px;top:310px"><div class="img" role="img" aria-label="University area streets"></div>University Area</div>
</section>

<section class="feeds">
  <div class="snap">
    <div class="mark" aria-label="Snapvane"></div>
    <div class="handle">tapwellhomefind.com</div>
    <div class="follow">Follow</div>
    <div class="stats">312 posts · 1,204 followers · 486 following</div>
    <div class="bio">Houston homes, market tips and open house news from your local realtor. Snapvane feed.<br>www.tapwellhomefind.com</div>
    <div class="grid">
      <div role="img" aria-label="Feed photo" style="background:#8ea3b6"></div>
      <div role="img" aria-label="Feed photo" style="background:#a7927a"></div>
      <div role="img" aria-label="Feed photo" style="background:#7c8a6a"></div>
      <div role="img" aria-label="Feed photo" style="background:#b9a995"></div>
      <div role="img" aria-label="Feed photo" style="background:#6f7f8f"></div>
      <div role="img" aria-label="Feed photo" style="background:#95a582"></div>
      <div role="img" aria-label="Feed photo" style="background:#a18a76"></div>
      <div role="img" aria-label="Feed photo" style="background:#84976f"></div>
      <div role="img" aria-label="Feed photo" style="background:#9aabbc"></div>
    </div>
  </div>
  <div class="friend">
    <div class="cover" role="img" aria-label="Friendloop page cover photo"></div>
    <div class="name">Friendloop · Calvin Brisk</div>
    <div class="line"></div><div class="line" style="width:100px"></div>
    <div class="pic" role="img" aria-label="Friendloop post photo"></div>
    <div class="line"></div><div class="line" style="width:90px"></div>
    <div class="pic" style="height:80px" role="img" aria-label="Friendloop post photo"></div>
  </div>
</section>

<footer class="footer">
  <div class="info">
    Brightpath Realty Memorial · 950 Quillbrook Lane, Houston, TX 77099 · 713-555-0148<br>
    Each Office is Independently Owned and Operated<br>
    Lone Star Property Licensing Board Consumer Protection Notice<br>
    Lone Star Property Licensing Board Information About Brokerage Services
  </div>
  <div class="rule"></div>
  <div>© 2019 Brightpath Realty · Terms of Use · Privacy Policy · Fair Housing · Site Map · Agent Login</div>
</footer>

</body>
</html>
```